Book Cover Design

Design with title UNWAVERING
Subtitle: Ways to Kindle the Spark of Resolve
Author Name: Carla Jean Morrow
Put DAILY MERIDIAN BESTSELLER at top
Shimmer design, see inspirational images attached

```html
<!DOCTYPE html>
<html lang="en">
<head>
<meta charset="utf-8">
<title>Unwavering — Carla Jean Morrow</title>
<link rel="stylesheet" href="https://fonts.googleapis.com/css2?family=Saira+Extra+Condensed:wght@100;200;300&display=swap">
<style>
  :root {
    --page-bg: #545454;
    --ink-plum: #5b1a6f;
    --ink-blue: #4a78b6;
    --sheen-lilac: #dcc4f2;
    --sheen-violet: #b4adf0;
    --sheen-sky: #9cc0f4;
    --sheen-ice: #e6eefb;
  }
  html, body {
    margin: 0;
    padding: 0;
    width: 1200px;
    height: 1077px;
    overflow: hidden;
    background: var(--page-bg);
  }
  .book-cover {
    position: absolute;
    left: 250px;
    top: 14px;
    width: 700px;
    height: 1049px;
    overflow: hidden;
    background:
      radial-gradient(ellipse 60% 22% at 15% 8%, rgba(231, 200, 248, 0.9), transparent 70%),
      radial-gradient(ellipse 40% 35% at 95% 20%, rgba(170, 170, 245, 0.8), transparent 70%),
      radial-gradient(ellipse 30% 80% at 50% 35%, rgba(246, 246, 250, 0.95), transparent 70%),
      radial-gradient(ellipse 55% 30% at 60% 100%, rgba(244, 248, 255, 0.95), transparent 70%),
      radial-gradient(ellipse 50% 40% at 5% 85%, rgba(140, 180, 245, 0.8), transparent 70%),
      linear-gradient(180deg, var(--sheen-lilac) 0%, var(--sheen-violet) 35%, var(--sheen-sky) 70%, var(--sheen-ice) 100%);
  }
  .cover-type {
    position: absolute;
    inset: 0;
    width: 100%;
    height: 100%;
    font-family: "Saira Extra Condensed", "Arial Narrow", sans-serif;
  }
  .bestseller-line { fill: var(--ink-plum); font-weight: 300; font-size: 60px; letter-spacing: 8px; }
  .author-name { fill: var(--ink-plum); font-weight: 300; font-size: 127px; letter-spacing: 10px; }
  .book-title { fill: var(--ink-blue); font-weight: 100; font-size: 313px; }
  .book-subtitle { fill: var(--ink-plum); font-weight: 300; font-size: 64px; letter-spacing: 9px; }
</style>
</head>
<body>
  <div class="book-cover">
    <svg class="cover-type" viewBox="0 0 700 1049" xmlns="http://www.w3.org/2000/svg">
      <text class="bestseller-line" x="350" y="98" text-anchor="middle" textLength="537" lengthAdjust="spacingAndGlyphs">DAILY MERIDIAN BESTSELLER</text>
      <text class="author-name" x="350" y="241" text-anchor="middle" textLength="579" lengthAdjust="spacingAndGlyphs">CARLA JEAN MORROW</text>
      <text class="book-title" x="350" y="518" text-anchor="middle" textLength="608" lengthAdjust="spacingAndGlyphs">UNWAVERING</text>
      <text class="book-subtitle" x="350" y="915" text-anchor="middle" textLength="444" lengthAdjust="spacingAndGlyphs">WAYS TO KINDLE THE</text>
      <text class="book-subtitle" x="350" y="980" text-anchor="middle" textLength="380" lengthAdjust="spacingAndGlyphs">SPARK OF RESOLVE</text>
    </svg>
  </div>
</body>
</html>
```